Modern Minimal Acne Clearing Set Retail Box

We need a design for our slide out packaging box. The packaging is for our Acne Clearing Set, which includes a cleanser and a cream. We would love something that's original,minimal and modern and not gender specific. Feel free to use your own take on design. Surprise us. I've attached dimensions of the box as well as some refrence images of some boxes we like. It doesn't have to be exactly like these images but its a good starting point. Ive also attached our logo (you can change the logo style if needed to fit your design), your free to use other fonts and colors to match your design. The back of the box will have the drug fact for both products.

Target Market(s)

Everybody

Industry/Entity Type

Beauty

Font styles to use
Sans Serif

Colors
3176b5
33a6d7
85cae6
33b8a4
86cfc6
1b1b1b
ececec

Requirements
Must have
• Originality

```html
<!DOCTYPE html>
<html lang="en">
<head>
<meta charset="utf-8">
<title>Acne Clearing Set – Dieline</title>
<link href="https://fonts.googleapis.com/css2?family=Crimson+Text&family=Montserrat:wght@400;500;600&display=swap" rel="stylesheet">
<style>
  :root {
    --sky: #85c0e6;
    --sky-soft: #8ec5e8;
    --ink: #1b1b1b;
    --cut: #222222;
    --guide: #b5b5b5;
    --paper: #ffffff;
    --pattern: #f1f3f6;
  }
  html, body { margin: 0; padding: 0; overflow: hidden; background: var(--paper); }
  .canvas { display: block; width: 1200px; height: 1186px; }
  .label { font-family: "Crimson Text", serif; font-size: 19px; fill: var(--ink); }
  .dim { font-family: "Crimson Text", serif; font-size: 10px; fill: var(--ink); text-anchor: middle; }
  .dim-side { text-anchor: start; }
  .cut { fill: none; stroke: var(--cut); stroke-width: 1; }
  .guide { fill: none; stroke: var(--guide); stroke-width: 1; }
  .panel-blue { fill: var(--sky); }
  .sans { font-family: "Montserrat", sans-serif; }
  .claim { font-size: 8px; font-weight: 600; fill: var(--paper); text-anchor: middle; letter-spacing: .3px; }
  .hero { font-size: 16px; font-weight: 500; fill: var(--paper); text-anchor: middle; letter-spacing: 4.5px; }
  .hero-side { fill: var(--sky); }
  .kit { font-size: 13.5px; font-weight: 600; fill: var(--paper); text-anchor: middle; letter-spacing: 2px; }
  .fine { font-size: 6px; fill: var(--paper); text-anchor: middle; }
  .fine-caps { font-size: 5.5px; font-weight: 600; letter-spacing: .8px; }
  .brand { font-size: 17px; font-weight: 600; fill: var(--paper); text-anchor: middle; letter-spacing: .5px; }
  .brand-band { stroke: var(--paper); stroke-width: 1; }
</style>
</head>
<body>
<svg class="canvas" viewBox="0 0 1500 1484" xmlns="http://www.w3.org/2000/svg">

  <!-- SLEEVE OUTSIDE -->
  <g class="sleeve-outside">
    <text class="label" x="63" y="21">sleeve outside</text>
    <text class="dim" x="187" y="40">76mm</text>
    <text class="dim" x="343" y="40">43mm</text>
    <text class="dim" x="495" y="40">76mm</text>
    <text class="dim" x="651" y="40">43mm</text>
    <text class="dim dim-side" x="727" y="283">165mm</text>

    <g class="guide">
      <path d="M51 0v35M90 0v35M289 0v35M401 0v35M600 0v35M712 0v35"/>
      <path d="M51 578v33M90 578v33M289 578v33M401 578v33M600 578v33M712 578v33"/>
      <path d="M0 52h35M0 91h35M0 522h35M0 561h35"/>
      <path d="M730 52h33M730 91h33M730 522h33M730 561h33"/>
    </g>

    <rect class="panel-blue" x="90" y="91" width="199" height="431"/>
    <rect class="panel-blue" x="401" y="91" width="199" height="431"/>

    <g class="cut">
      <rect x="51" y="52" width="661" height="509"/>
      <path d="M51 91h661M51 522h661M90 52v509M289 52v509M401 52v509M600 52v509"/>
    </g>

    <g class="front-panel sans">
      <text class="claim" x="190" y="125">ACNE CLEARING SYSTEM</text>
      <text class="claim" x="190" y="135">AND ANTIMICROBIAL</text>
      <text class="hero" transform="translate(196 275) rotate(-90)">INTENSE CLEARING</text>
      <text class="kit" x="191" y="422">2 IN ONE KIT</text>
      <text class="fine" x="191" y="437">Suitable for</text>
      <text class="fine" x="191" y="445">Combination, Dry &amp; Normal skin</text>
      <text class="fine fine-caps" x="191" y="453">FOR VISIBLY CLEARER SKIN</text>
      <text class="brand" x="191" y="497">Petal Lab</text>
    </g>

    <g class="front-panel sans">
      <text class="claim" x="501" y="125">ACNE CLEARING SYSTEM</text>
      <text class="claim" x="501" y="135">AND ANTIMICROBIAL</text>
      <text class="hero" transform="translate(507 275) rotate(-90)">INTENSE CLEARING</text>
      <text class="kit" x="502" y="422">2 IN ONE KIT</text>
      <text class="fine" x="502" y="437">Suitable for</text>
      <text class="fine" x="502" y="445">Combination, Dry &amp; Normal skin</text>
      <text class="fine fine-caps" x="502" y="453">FOR VISIBLY CLEARER SKIN</text>
      <text class="brand" x="502" y="497">Petal Lab</text>
    </g>

    <text class="sans hero hero-side" transform="translate(350 308) rotate(-90)">INTENSE CLEARING</text>
    <text class="sans hero hero-side" transform="translate(652 310) rotate(90)">INTENSE CLEARING</text>
  </g>

  <!-- SLEEVE INSIDE -->
  <g class="sleeve-inside">
    <text class="label" x="838" y="21">sleeve inside</text>
    <rect x="835" y="91" width="661" height="431" fill="var(--pattern)" role="img" aria-label="Repeating diagonal brand-name pattern in pale grey and light blue"/>
    <g class="cut">
      <rect x="835" y="91" width="661" height="431"/>
      <path d="M947 91v431M1146 91v431M1258 91v431M1457 91v431"/>
    </g>
  </g>

  <!-- TRAY OUTSIDE -->
  <g class="tray-outside">
    <text class="label" x="96" y="713">tray outside</text>
    <text class="dim" x="430" y="700">70mm</text>
    <text class="dim dim-side" x="715" y="814">38mm</text>
    <text class="dim dim-side" x="715" y="1088">162mm</text>
    <text class="dim dim-side" x="715" y="1348">38mm</text>

    <g class="guide">
      <path d="M202 682v33M242 682v33M341 682v33M524 682v33M662 682v33"/>
      <path d="M202 1448v36M242 1448v36M341 1448v36M524 1448v36M662 1448v36"/>
      <path d="M152 731h34M152 770h34M152 869h34M152 1293h34M152 1392h34M152 1431h34"/>
      <path d="M679 731h34M679 770h34M679 869h34M679 1293h34M679 1392h34M679 1431h34"/>
      <rect x="341" y="731" width="183" height="138"/>
      <path d="M341 770h183"/>
      <rect x="341" y="1293" width="183" height="138"/>
      <path d="M341 1392h183"/>
      <rect x="202" y="869" width="40" height="424"/>
      <rect x="623" y="869" width="39" height="424"/>
    </g>
    <g class="cut">
      <rect x="242" y="869" width="381" height="424"/>
      <path d="M341 869v424M524 869v424"/>
    </g>

    <text class="sans hero hero-side" transform="translate(296 1082) rotate(-90)">INTENSE CLEARING</text>
    <text class="sans hero hero-side" transform="translate(571 1080) rotate(90)">INTENSE CLEARING</text>
  </g>

  <!-- TRAY INSIDE -->
  <g class="tray-inside">
    <text class="label" x="975" y="732">tray inside</text>
    <rect x="1125" y="869" width="183" height="424" fill="var(--sky-soft)" role="img" aria-label="Light blue panel with faint repeating brand-name pattern"/>
    <g class="guide">
      <rect x="1026" y="869" width="381" height="424"/>
      <rect x="1125" y="770" width="183" height="622"/>
    </g>
    <path class="brand-band" d="M1125 883h183M1125 929h183"/>
    <text class="sans brand" x="1216" y="913">Petal Lab</text>
  </g>
</svg>
</body>
</html>
```